Tech Enablement - Trifold

I need at trifold for marketing outreach /collateral for our technology enablement as a service offering.
Details provided in attached doc.

```html
<!DOCTYPE html>
<html lang="en">
<head>
<meta charset="utf-8">
<title>Norvanta – Technology Enablement Trifold</title>
<link rel="stylesheet" href="https://fonts.googleapis.com/css2?family=Montserrat:wght@400;500;600;700;800&family=Oswald:wght@300;400&family=Libre+Baskerville:ital@1&display=swap">
<style>
:root{
  --sheet:#2b2e30;
  --blue:#0b8fcc;
  --blue-bright:#1196d4;
  --navy:#1b4a68;
  --navy-deep:#173f5a;
  --teal-ring:#3d7592;
  --paper:#ffffff;
  --paper-light:#e8edf0;
  --ink:#1f2a33;
  --ink-head:#1c3d55;
}
*{box-sizing:border-box}
html,body{margin:0;padding:0;overflow:hidden}
body{width:1046px;height:1200px;background:var(--sheet);position:relative;font-family:"Montserrat",Arial,sans-serif;color:var(--ink)}

.sheet-label{position:absolute;color:#fff;font:800 17px "Montserrat",sans-serif;letter-spacing:6px;transform:translateX(-50%);margin:0}

.panel{position:absolute;overflow:hidden}
.panel--white{background:var(--paper)}
.panel--light{background:var(--paper-light)}

.wordmark{position:absolute;display:flex;align-items:center;gap:6px;font:600 22px "Montserrat",sans-serif;letter-spacing:1.5px}
.wordmark__dot{width:14px;height:14px;border-radius:50%;background:currentColor;flex:none}
.wordmark--blue{color:var(--blue)}
.wordmark--white{color:#fff}
.wordmark--small{font-size:18px;gap:5px}
.wordmark--small .wordmark__dot{width:11px;height:11px}

.prod-head{display:flex;align-items:flex-start;gap:7px}
.prod-num{font-family:"Oswald",sans-serif;color:var(--ink-head);line-height:1;padding-right:6px;border-right:1px dotted #8a99a5;align-self:stretch}
.prod-num small{display:block;font-size:6.5px;font-weight:400;letter-spacing:.2px}
.prod-num strong{display:block;font-size:27px;font-weight:400;margin-top:1px}
.prod-title{font:800 14px/17px "Montserrat",sans-serif;color:var(--blue);margin:0}
.prod-title em{font:italic 5.8px "Libre Baskerville",serif;color:var(--ink-head)}
.prod-note{display:block;font:italic 5.8px "Libre Baskerville",serif;color:var(--ink-head);margin-top:2px}

.lede{font:400 13px/16px "Oswald",sans-serif;color:var(--ink-head);margin:0;letter-spacing:-.2px}

.tag{display:inline-block;background:var(--navy);color:#fff;font:500 9.5px/1 "Montserrat",sans-serif;padding:5px 16px 5px 9px;border-radius:0 11px 11px 0;margin:0}
.tag--white{background:#fff;color:var(--navy-deep)}

.ticks{list-style:none;margin:0;padding:0 0 0 10px}
.ticks li{position:relative;padding-left:10px;font-size:8.3px;line-height:11px;color:var(--ink)}
.ticks li::before{content:"";position:absolute;left:0;top:2px;width:7px;height:7px;border-radius:50%;background:var(--blue)}
.ticks li::after{content:"";position:absolute;left:2.3px;top:3.2px;width:2px;height:3.4px;border:solid #fff;border-width:0 1.1px 1.1px 0;transform:rotate(45deg)}
.ticks .sub{padding-left:17px}
.ticks .sub::before{left:7px}
.ticks .sub::after{left:9.3px}
.ticks--light li{color:#fff}
.ticks--light li::before{background:#fff}
.ticks--light li::after{border-color:var(--blue)}

.block{margin-top:8px}
.block .ticks{margin-top:6px}

.compact .block{margin-top:6px}
.compact .block .ticks{margin-top:5px}
.compact .ticks li{line-height:10.6px}

.cta{position:absolute;left:24px;width:171px;height:120px;background:var(--navy-deep)}
.cta__line{margin:16px 0 0;color:#fff;text-align:center;font:700 12px/15px "Montserrat",sans-serif}
.cta__button{position:absolute;left:-7px;top:66px;width:185px;height:39px;background:var(--blue-bright);color:#fff;text-align:center;font:600 11px/14px "Montserrat",sans-serif;padding-top:6px;margin:0}

.cover{background:linear-gradient(180deg,#0c8fd0 0%,#1a6690 40%,#1d5876 62%,#1478ac 82%,#0c8fd0 100%)}
.cover__photo{position:absolute;left:12px;top:74px;width:207px;height:302px;border-radius:0 0 104px 104px;background:linear-gradient(180deg,#4f8fb8 0%,#1f4f72 35%,#122c44 70%,#1c3a55 100%);border:3px solid #fff}
.cover__title{position:absolute;left:0;right:0;top:384px;margin:0;text-align:center;color:#fff;font:800 19.5px/22px "Montserrat",sans-serif}
.cover__sub{position:absolute;left:0;right:0;top:476px;margin:0;text-align:center;color:#fff;font:italic 10.5px/14px "Libre Baskerville",serif}

.problem{background:linear-gradient(180deg,#1e5373 0%,#1a6a95 50%,#0f86c3 100%);color:#fff}
.problem__title{position:absolute;left:25px;top:108px;margin:0;font:800 13px "Montserrat",sans-serif}
.problem__lede{position:absolute;left:25px;top:130px;margin:0;font:400 12px/16px "Oswald",sans-serif;letter-spacing:-.3px}
.pain-grid{position:absolute;left:16px;top:208px;width:200px;display:grid;grid-template-columns:repeat(3,1fr);row-gap:10px}
.pain{display:flex;flex-direction:column;align-items:center;text-align:center;border-left:1px dashed rgba(255,255,255,.5);height:92px}
.pain:nth-child(3n+1){border-left:none}
.pain__icon{width:47px;height:47px}
.pain__label{font-size:7.6px;line-height:10px;margin:6px 0 0;color:#e8f4fb}

.approach__title{position:absolute;left:22px;top:244px;margin:0;font:800 14px/17px "Montserrat",sans-serif;color:var(--ink-head)}
.approach__title span{color:var(--blue)}
.closing{font:400 12px "Oswald",sans-serif;color:var(--ink-head);margin:0}
.closing b{font-weight:400;letter-spacing:.1px;text-shadow:0 0 .4px var(--ink-head)}
</style>
</head>
<body>

<h2 class="sheet-label" style="left:391px;top:20px">OUTSIDE</h2>
<h2 class="sheet-label" style="left:877px;top:20px">COVER</h2>
<h2 class="sheet-label" style="left:391px;top:597px">INSIDE</h2>
<h2 class="sheet-label" style="left:877px;top:597px">BACK</h2>

<!-- OUTSIDE: product 02 -->
<section class="panel panel--white" style="left:53px;top:48px;width:224px;height:528px">
  <svg style="position:absolute;left:0;top:395px" width="224" height="133" viewBox="0 0 224 133">
    <defs><linearGradient id="laptopTone" x1="0" y1="0" x2="1" y2="1"><stop offset="0" stop-color="#6b4a32"/><stop offset=".5" stop-color="#3a3230"/><stop offset="1" stop-color="#1b3e58"/></linearGradient></defs>
    <rect width="224" height="133" fill="url(#laptopTone)" role="img" aria-label="Photo of hands typing on a laptop with glowing technology icons"/>
    <path d="M0 0 H224 V4 C200 55 160 70 112 72 C64 70 24 55 0 4 Z" fill="#0b8fcc"/>
    <path d="M0 0 H224 V0 C198 48 158 62 112 64 C66 62 26 48 0 0 Z" fill="#fff"/>
  </svg>
  <div class="compact" style="position:absolute;left:23px;top:18px;width:195px">
    <div class="prod-head">
      <div class="prod-num"><small>PRODUCT</small><strong>02</strong></div>
      <h3 class="prod-title">Technology<br>Enablement as<br>a Service <em>(The Core Offering)</em></h3>
    </div>
    <p class="lede" style="margin-top:5px">Turn clarity into action — at your pace.</p>
    <div class="block" style="margin-top:8px">
      <p class="tag">What it is</p>
      <ul class="ticks"><li>Ongoing enablement support</li><li>No per-seat pricing</li><li>No traditional IT contract</li></ul>
    </div>
    <div class="block">
      <p class="tag">What it includes</p>
      <ul class="ticks"><li>Strategic technology oversight</li><li>Living roadmap management</li><li>Workflow and process improvement</li><li>Adoption and change support</li><li>Vendor and tool coordination</li><li>Execution guidance across tools, data, and automation</li></ul>
    </div>
    <div class="block">
      <p class="tag">How it's priced</p>
      <ul class="ticks"><li><b style="font-weight:600">Starting at a base level</b></li><li>Scales based on:</li><li class="sub">Speed of execution</li><li class="sub">Complexity of initiatives</li><li class="sub">Desired pace of improvement</li></ul>
    </div>
    <div class="block">
      <p class="tag">This is where</p>
      <ul class="ticks"><li>Improvements actually happen</li><li>Adoption sticks</li><li>Systems begin to work together</li></ul>
    </div>
  </div>
</section>

<!-- OUTSIDE: product 03 -->
<section class="panel panel--light" style="left:277px;top:48px;width:224px;height:528px">
  <div class="wordmark wordmark--blue" style="left:40px;top:31px"><span class="wordmark__dot"></span>NORVANTA</div>
  <div style="position:absolute;left:26px;top:106px;width:190px">
    <div class="prod-head">
      <div class="prod-num"><small>PRODUCT</small><strong>03</strong></div>
      <div><h3 class="prod-title">Execution<br>&amp; Managed IT</h3><span class="prod-note">(The Natural Evolution)</span></div>
    </div>
    <p class="lede" style="margin-top:10px">When execution and trust are established, deeper partnership follows.</p>
    <div class="block" style="margin-top:10px">
      <p class="tag">What Product 3 represents</p>
      <ul class="ticks"><li>Confident execution</li><li>Deeper technical ownership</li><li>Managed IT and infrastructure support</li></ul>
    </div>
    <div class="block">
      <p class="tag">Why this comes last</p>
      <ul class="ticks"><li>Clients already trust the roadmap</li><li>Norvanta understands the business</li><li>Decisions are informed, not reactive</li></ul>
    </div>
    <p class="lede" style="margin-top:8px;font-size:12px;line-height:15px">Product 3 is not pushed<br>it's earned through results and relationship.</p>
  </div>
  <div class="cta" style="top:373px">
    <p class="cta__line">Start with clarity.<br>Build with confidence.<br>Scale with control.</p>
    <p class="cta__button">Book a Technology<br>Enablement Assessment</p>
  </div>
</section>

<!-- OUTSIDE: front cover -->
<section class="panel cover" style="left:501px;top:48px;width:231px;height:528px">
  <div class="wordmark wordmark--white" style="left:42px;top:31px"><span class="wordmark__dot"></span>NORVANTA</div>
  <div class="cover__photo" role="img" aria-label="Photo of a team working at laptops in a modern office with a world map display"></div>
  <h1 class="cover__title">Technology<br>Enablement for<br>Growing<br>Businesses</h1>
  <p class="cover__sub">Turn disconnected tools into systems<br>that actually work</p>
</section>

<!-- COVER -->
<section class="panel cover" style="left:765px;top:48px;width:231px;height:527px">
  <div class="wordmark wordmark--white" style="left:42px;top:31px"><span class="wordmark__dot"></span>NORVANTA</div>
  <div class="cover__photo" role="img" aria-label="Photo of a team working at laptops in a modern office with a world map display"></div>
  <h1 class="cover__title">Technology<br>Enablement for<br>Growing<br>Businesses</h1>
  <p class="cover__sub">Turn disconnected tools into systems<br>that actually work</p>
</section>

<!-- INSIDE spread -->
<section class="panel" style="left:53px;top:627px;width:679px;height:527px">
  <div class="panel problem" style="left:0;top:0;width:231px;height:527px">
    <div class="wordmark wordmark--white wordmark--small" style="left:25px;top:61px"><span class="wordmark__dot"></span>NORVANTA</div>
    <h2 class="problem__title">The Problem We Solve</h2>
    <p class="problem__lede">Most businesses don't have a technology<br>problem. They have an enablement problem.</p>
    <svg style="position:absolute;left:0;top:176px" width="231" height="30" viewBox="0 0 231 30">
      <path d="M90 10 H205 Q214 10 214 19 V21" fill="none" stroke="#fff" stroke-width=".8"/>
      <circle cx="214" cy="22" r="2.2" fill="#fff"/>
    </svg>
    <p class="tag tag--white" style="position:absolute;left:25px;top:178px">What it is</p>
    <div class="pain-grid">
      <div class="pain">
        <svg class="pain__icon" viewBox="0 0 48 48"><circle cx="24" cy="24" r="22.5" fill="#1891cf" stroke="#fff" stroke-width="1.5"/><rect x="14" y="15" width="20" height="13" fill="none" stroke="#fff" stroke-width="1.3"/><path d="M24 28v5M19 33h10" stroke="#fff" stroke-width="1.3"/></svg>
        <p class="pain__label">Plenty of software, no real system</p>
      </div>
      <div class="pain">
        <svg class="pain__icon" viewBox="0 0 48 48"><circle cx="24" cy="24" r="22.5" fill="#1891cf" stroke="#fff" stroke-width="1.5"/><circle cx="24" cy="24" r="8" fill="none" stroke="#fff" stroke-width="3" stroke-dasharray="3 2"/><circle cx="24" cy="24" r="3.5" fill="none" stroke="#fff" stroke-width="1.3"/></svg>
        <p class="pain__label">Manual work filling the gaps</p>
      </div>
      <div class="pain">
        <svg class="pain__icon" viewBox="0 0 48 48"><circle cx="24" cy="24" r="22.5" fill="#1891cf" stroke="#fff" stroke-width="1.5"/><rect x="14" y="16" width="20" height="6" rx="3" fill="none" stroke="#fff" stroke-width="1.2"/><rect x="14" y="26" width="20" height="6" rx="3" fill="none" stroke="#fff" stroke-width="1.2"/><circle cx="30" cy="19" r="1.8" fill="#fff"/><circle cx="18" cy="29" r="1.8" fill="#fff"/></svg>
        <p class="pain__label">Processes living in people's heads</p>
      </div>
      <div class="pain">
        <svg class="pain__icon" viewBox="0 0 48 48"><circle cx="24" cy="24" r="22.5" fill="#1891cf" stroke="#fff" stroke-width="1.5"/><circle cx="24" cy="24" r="10" fill="none" stroke="#fff" stroke-width="1.3"/><path d="M19.5 24l3 3 6-6" fill="none" stroke="#fff" stroke-width="1.5"/></svg>
        <p class="pain__label">Poor adoption of tools already paid for</p>
      </div>
      <div class="pain">
        <svg class="pain__icon" viewBox="0 0 48 48"><circle cx="24" cy="24" r="22.5" fill="#1891cf" stroke="#fff" stroke-width="1.5"/><path d="M13 30a11 11 0 0 1 22 0" fill="none" stroke="#fff" stroke-width="1.4"/><path d="M24 30l5-7" stroke="#fff" stroke-width="1.4"/><circle cx="24" cy="30" r="1.8" fill="#fff"/></svg>
        <p class="pain__label">Limited visibility into performance</p>
      </div>
      <div class="pain">
        <svg class="pain__icon" viewBox="0 0 48 48"><circle cx="24" cy="24" r="22.5" fill="#1891cf" stroke="#fff" stroke-width="1.5"/><circle cx="24" cy="21" r="7" fill="none" stroke="#fff" stroke-width="1.3"/><path d="M21 30h6M22 33h4" stroke="#fff" stroke-width="1.3"/></svg>
        <p class="pain__label">Reactive technology decisions</p>
      </div>
    </div>
    <svg style="position:absolute;left:0;top:414px" width="231" height="30" viewBox="0 0 231 30">
      <path d="M90 10 H205 Q214 10 214 19 V21" fill="none" stroke="#fff" stroke-width=".8"/>
      <circle cx="214" cy="22" r="2.2" fill="#fff"/>
    </svg>
    <p class="tag tag--white" style="position:absolute;left:25px;top:416px">The result</p>
    <ul class="ticks ticks--light" style="position:absolute;left:16px;top:441px;width:190px">
      <li style="margin-bottom:3px">More effort, more admin, less return on software spend.</li>
      <li>This pain should feel <b>instantly recognizable</b></li>
    </ul>
  </div>

  <div class="panel panel--white" style="left:231px;top:0;width:224px;height:527px">
    <h2 class="approach__title">Our Approach:<br><span>Technology Enablement</span></h2>
    <div style="position:absolute;left:22px;top:284px;width:196px">
      <p class="lede">Technology Enablement improves how work flows through your business.</p>
      <div class="block" style="margin-top:10px">
        <p class="tag">Norvanta focuses on</p>
        <ul class="ticks"><li>Workflows before tools</li><li>Adoption before automation</li><li>Outcomes before technology decisions</li></ul>
      </div>
      <div class="block">
        <p class="tag">What makes us different</p>
        <ul class="ticks"><li>No requirement to replace systems</li><li>No need to change IT providers</li><li>No long-term contracts</li><li>Clarity first, execution only where it makes sense</li></ul>
      </div>
      <p class="closing" style="margin-top:6px">This panel establishes <b>trust and differentiation</b></p>
    </div>
  </div>

  <div class="panel panel--white" style="left:455px;top:0;width:224px;height:527px">
    <div style="position:absolute;left:23px;top:147px;width:196px">
      <div class="prod-head">
        <div class="prod-num"><small>PRODUCT</small><strong>01</strong></div>
        <h3 class="prod-title">Technology<br>Enablement<br>Assessment <em>(The Entry Point)</em></h3>
      </div>
      <p class="lede" style="margin-top:4px">Start with clarity.</p>
      <div class="block" style="margin-top:8px">
        <p class="tag">What it is</p>
        <ul class="ticks"><li>2–4 week, stand-alone assessment</li><li>Fixed scope, fixed price</li><li>Low risk, high insight</li></ul>
      </div>
      <div class="block">
        <p class="tag">What we assess</p>
        <ul class="ticks"><li>Workflows and handoffs</li><li>Technology and digital maturity</li><li>Adoption and training gaps</li><li>Automation and integration opportunities</li><li>Data, reporting, and KPI visibility</li></ul>
      </div>
      <div class="block">
        <p class="tag">What you receive</p>
        <ul class="ticks"><li>A prioritized Improvement Roadmap</li><li>Clear business impact and effort</li><li>Confidence before spending more money</li></ul>
      </div>
      <p class="lede" style="margin-top:10px;font-size:12.5px;line-height:16px">Purpose of Product 1:<br>Designed to create insight, trust, and<br>momentum — not a forced upsell.</p>
    </div>
  </div>

  <svg style="position:absolute;left:0;top:0" width="679" height="230" viewBox="0 0 679 230">
    <defs>
      <linearGradient id="tabletTone" x1="0" y1="0" x2="1" y2="1"><stop offset="0" stop-color="#0e4a66"/><stop offset=".45" stop-color="#1b6f8c"/><stop offset="1" stop-color="#0f2336"/></linearGradient>
      <linearGradient id="dealTone" x1="0" y1="0" x2="1" y2="1"><stop offset="0" stop-color="#2c4a66"/><stop offset="1" stop-color="#0d1a2c"/></linearGradient>
    </defs>
    <path d="M541 0 L679 0 L679 92 Q600 100 482 130 Q530 80 541 0 Z" fill="url(#dealTone)" role="img" aria-label="Photo of a digital handshake over a city skyline at night"/>
    <path d="M152 0 C200 90 262 180 346 207 C430 180 492 90 547 0 Z" fill="#3d7592"/>
    <path d="M172 0 C218 80 272 165 346 196 C420 165 474 80 527 0 Z" fill="url(#tabletTone)" role="img" aria-label="Photo of a businessman using a tablet with a glowing digital interface"/>
  </svg>
</section>

<!-- BACK -->
<section class="panel panel--light" style="left:765px;top:627px;width:224px;height:527px">
  <div class="wordmark wordmark--blue" style="left:36px;top:31px"><span class="wordmark__dot"></span>NORVANTA</div>
  <div style="position:absolute;left:26px;top:106px;width:192px">
    <div class="prod-head">
      <div class="prod-num"><small>PRODUCT</small><strong>03</strong></div>
      <div><h3 class="prod-title">Execution<br>&amp; Managed IT</h3><span class="prod-note">(The Natural Evolution)</span></div>
    </div>
    <p class="lede" style="margin-top:10px">When execution and trust are established, deeper partnership follows.</p>
    <div class="block" style="margin-top:10px">
      <p class="tag">What Product 3 represents</p>
      <ul class="ticks"><li>Confident execution</li><li>Deeper technical ownership</li><li>Managed IT and infrastructure support</li></ul>
    </div>
    <div class="block">
      <p class="tag">Why this comes last</p>
      <ul class="ticks"><li>Clients already trust the roadmap</li><li>Norvanta understands the business</li><li>Decisions are informed, not reactive</li></ul>
    </div>
    <p class="lede" style="margin-top:8px;font-size:12px;line-height:15px">Product 3 is not pushed<br>it's earned through results and relationship.</p>
  </div>
  <div class="cta" style="top:373px">
    <p class="cta__line">Start with clarity.<br>Build with confidence.<br>Scale with control.</p>
    <p class="cta__button">Book a Technology<br>Enablement Assessment</p>
  </div>
</section>

</body>
</html>
```